Clinic for cellulit and fat removal

Name of clinic :
Lumera
- Body & Health (this has to be written on the site.)
I need CMS for me to be able to make changes myself.
A webpage for woman searching for a solution to remove fat and cellulit.
The owner is a brazilian woman in Denmark, and want her sense of aestetic shines thru the website.
There needs to be a slide show on the landing page showing big sliding pictures, of the clinic and and the treatments.
The Cryolipolysis, is a treatment freezing fat and cellulit, and this treatment will be the Attraction of the clinic.
Needs These pages in a horisontal fasion. (written in Danish)
Lumera
Behandlinger
- Cryolipolysis
- Silkora
- Lymfemassage
- Tandrelia
- Copper Tide
Produkter
Priser
Kontakt

```html
<!DOCTYPE html>
<html lang="en">
<head>
<meta charset="utf-8">
<title>Lumera – Body &amp; Health</title>
<link href="https://fonts.googleapis.com/css2?family=Roboto:wght@400;500;700&family=Open+Sans:wght@400;600&display=swap" rel="stylesheet">
<style>
:root{
  --blue:#1eaee8;
  --blue-dark:#0f8fcf;
  --blue-light:#dff3fc;
  --orange:#f5aa1e;
  --orange-dark:#e79812;
  --ink:#2b2b2b;
  --muted:#555;
  --footer:#616161;
  --white:#fff;
}
*{margin:0;padding:0;box-sizing:border-box}
html,body{width:1200px;height:2731px;overflow:hidden;background:var(--white)}
body{position:relative;font-family:"Open Sans",Arial,sans-serif;color:var(--ink)}
.abs{position:absolute}
.heading{font-family:"Roboto",Arial,sans-serif;font-weight:500}

/* header */
.site-header{position:absolute;left:0;top:0;width:1200px;height:138px;background:var(--white);box-shadow:0 2px 6px rgba(0,0,0,.08);z-index:2}
.brand{position:absolute;left:91px;top:42px;display:flex;align-items:center;gap:12px}
.brand-dot{width:54px;height:54px;border-radius:50%;background:var(--blue)}
.brand-name{font-family:"Roboto",Arial,sans-serif;font-weight:500;font-size:38px;color:var(--orange)}
.lang{position:absolute;left:615px;top:27px;width:96px;height:33px;border:1px solid #bbb;display:flex;align-items:center;gap:6px;padding-left:5px;font:400 15px "Roboto",sans-serif}
.lang-swatch{width:34px;height:22px;background:#2d3f86}
.lang-caret{width:0;height:0;border-left:5px solid transparent;border-right:5px solid transparent;border-top:6px solid #333}
.contact-item{position:absolute;top:25px;display:flex;align-items:center;gap:12px;font:500 18px "Roboto",sans-serif}
.contact-icon{width:34px;height:34px;border-radius:50%;display:flex;align-items:center;justify-content:center}
.nav{position:absolute;top:87px;left:448px;display:flex;font:500 15px "Roboto",sans-serif;color:#222}
.nav a{text-decoration:none;color:inherit;position:absolute;top:0;height:37px;line-height:37px;white-space:nowrap}
.nav .active{background:var(--orange);color:#fff;border-radius:19px;padding:0 15px}

/* hero */
.hero{position:absolute;left:0;top:138px;width:1200px;height:712px;background:linear-gradient(100deg,#1ea5e6 0%,#48bdf0 40%,#cfeefb 70%,#eaf7fd 100%);overflow:hidden}
.hero-photo{position:absolute;left:783px;top:0;width:417px;height:490px;background:radial-gradient(ellipse at 55% 45%,#f1cdb8 0%,#e8b9a0 35%,rgba(233,244,251,0) 70%)}
.hero-pill{position:absolute;left:175px;top:95px;width:440px;height:78px;border-radius:39px;background:var(--orange);color:#fff;font:500 44px "Roboto",sans-serif;text-align:center;line-height:78px;letter-spacing:1px}
.hero-text{position:absolute;left:80px;top:209px;width:640px;text-align:center;color:#fff;font-size:16px;line-height:28px}
.btn-outline{position:absolute;border:2px solid #fff;color:#fff;font-size:17px;text-align:center}
.hero-arrow{position:absolute;top:215px}
.feature{position:absolute;color:#fff}
.feature h3{font:500 27px "Roboto",sans-serif;margin-bottom:18px}
.feature p{font-size:14px;line-height:24px;width:460px}

/* about */
.section-title{position:absolute;left:0;width:1200px;text-align:center;font:500 29px "Roboto",sans-serif;color:var(--blue)}
.title-rule{position:absolute;left:554px;width:92px;height:3px;background:var(--blue)}
.about-text{position:absolute;left:150px;top:1008px;width:900px;text-align:center;font-size:13px;line-height:26px;color:#333}
.btn{position:absolute;height:43px;line-height:41px;text-align:center;font:500 16px "Roboto",sans-serif}
.btn-orange{background:var(--orange);color:#fff}
.btn-dark{border:2px solid #222;color:#222}

/* cryo */
.cryo{position:absolute;left:0;top:1242px;width:1200px;height:452px;background:linear-gradient(90deg,#f3a51c,#f7b532 60%,#f3a51c)}
.cryo h2{position:absolute;left:89px;top:68px;font:500 29px "Roboto",sans-serif;color:#fff}
.cryo h4{position:absolute;left:89px;top:140px;font:500 17px "Roboto",sans-serif;color:#fff}
.cryo p{position:absolute;left:89px;top:180px;width:468px;font-size:13px;line-height:22.5px;color:#fff;text-align:justify}
.video{position:absolute;left:599px;top:73px;width:501px;height:300px;border:3px solid #fff;background:linear-gradient(135deg,#cbb5a6,#8c7a70 50%,#e6e3e0)}
.play{position:absolute;left:197px;top:117px;width:62px;height:62px;border-radius:50%;border:3px solid #fff;background:rgba(0,0,0,.35)}

/* testimonials */
.quote{position:absolute;top:1856px;width:304px;height:174px;border:2px solid var(--orange);border-radius:6px;background:#fff;padding:22px 22px 0 48px;font-style:italic;font-size:13px;line-height:23px;color:#444;text-align:justify}
.quote.featured{background:var(--blue);border-color:var(--blue);color:#fff}
.quote-mark{position:absolute;left:14px;top:10px;font:700 40px Georgia,serif;color:var(--orange);line-height:1}
.quote.featured .quote-mark{color:#fff}
.quote-tail{position:absolute;left:26px;bottom:-14px;width:22px;height:22px;background:inherit;border-right:2px solid var(--orange);border-bottom:2px solid var(--orange);transform:rotate(45deg) skew(8deg,8deg)}
.quote.featured .quote-tail{border-color:var(--blue)}
.author{position:absolute;top:2056px;display:flex;align-items:center;gap:16px}
.avatar{width:62px;height:62px;border-radius:50%;border:3px solid var(--orange);background:#e5d2c4}
.author.featured .avatar{border-color:var(--blue)}
.author-name{font:500 16px "Roboto",sans-serif;color:#222}
.author-date{font-size:12px;color:#777;margin-top:4px}

/* footer */
.footer{position:absolute;left:0;top:2247px;width:1200px;height:484px;background:var(--footer);color:#fff}
.info-strip{position:absolute;top:2209px;left:89px;width:1002px;height:98px;display:flex}
.info-cell{flex:1;display:flex;align-items:flex-start;padding:22px 0 0 36px;gap:22px;background:var(--blue)}
.info-cell.mid{background:var(--blue-dark)}
.info-icon{width:48px;height:48px;border:2px solid #fff;border-radius:50%;flex:none;display:flex;align-items:center;justify-content:center;margin-top:4px}
.info-cell h5{font:500 15px "Roboto",sans-serif;margin-bottom:8px}
.info-cell p{font-size:12px;line-height:18px}
.footer-brand{position:absolute;left:91px;top:2465px;display:flex;align-items:center;gap:12px}
.footer-brand .brand-name{color:#fff;font-size:44px}
.footer-col h6{font:500 17px "Roboto",sans-serif;letter-spacing:.5px}
.footer-col .rule{width:68px;height:2px;background:#fff;margin:12px 0 22px}
.footer-col li{list-style:none;font-size:14px;margin-bottom:14px}
.field{position:absolute;border:1px solid #ddd;border-radius:3px;font-size:10px;padding:8px 12px;color:#eee}
.send{position:absolute;left:821px;top:2548px;width:120px;height:38px;background:var(--blue);border:1px solid #fff;font:500 11px "Roboto",sans-serif;text-align:center;line-height:36px}
.footer-rule{position:absolute;left:89px;top:2655px;width:1002px;height:1px;background:#888}
.copyright{position:absolute;left:89px;top:2685px;font-size:13px}
.social{position:absolute;top:2677px;width:33px;height:33px;border:2px solid #fff;border-radius:50%}
</style>
</head>
<body>

<header class="site-header">
  <div class="brand"><span class="brand-dot"></span><span class="brand-name">Lumera</span></div>
  <div class="lang"><span class="lang-swatch" role="img" aria-label="English language flag"></span>Eng<span class="lang-caret"></span></div>
  <div class="contact-item" style="left:759px;color:var(--blue)">
    <span class="contact-icon" style="background:var(--blue)"><svg width="16" height="16" viewBox="0 0 24 24"><path fill="#fff" d="M6.6 10.8a15 15 0 006.6 6.6l2.2-2.2c.3-.3.7-.4 1-.2 1.1.4 2.3.6 3.6.6.6 0 1 .4 1 1V20c0 .6-.4 1-1 1A17 17 0 013 4c0-.6.4-1 1-1h3.5c.6 0 1 .4 1 1 0 1.3.2 2.5.6 3.6.1.3 0 .7-.2 1z"/></svg></span>140 318 7720
  </div>
  <div class="contact-item" style="left:913px;color:var(--orange)">
    <span class="contact-icon" style="background:var(--orange)"><svg width="16" height="16" viewBox="0 0 24 24"><circle cx="12" cy="12" r="9" fill="none" stroke="#fff" stroke-width="2"/><path d="M12 7v5l3 2" stroke="#fff" stroke-width="2" fill="none"/></svg></span>info@lumera.com
  </div>
  <nav class="nav">
    <a class="active" style="left:0">LUMERA</a>
    <a style="left:135px">BEHANDLINGER</a>
    <a style="left:313px">PRODUKTER</a>
    <a style="left:466px">PRISER</a>
    <a style="left:575px">KONTAKT</a>
  </nav>
</header>

<section class="hero">
  <div class="hero-photo" role="img" aria-label="Woman's toned torso with treatment marking arrows"></div>
  <div class="hero-pill">"BODY &amp; HEALTH"</div>
  <p class="hero-text">The Cryolipolysis, is a treatment freezing fat and cellulit, and this treatment will be the Attraction of the clinic.</p>
  <div class="btn-outline" style="left:335px;top:294px;width:120px;height:51px;line-height:47px">Read More</div>
  <svg class="hero-arrow" style="left:22px" width="34" height="70" viewBox="0 0 34 70"><path d="M32 2L2 35l30 33" fill="none" stroke="#fff" stroke-width="2"/></svg>
  <svg class="hero-arrow" style="left:1134px" width="34" height="70" viewBox="0 0 34 70"><path d="M2 2l30 33-30 33" fill="none" stroke="#fff" stroke-width="2" opacity=".8"/></svg>

  <svg class="abs" style="left:0;top:454px" width="1200" height="258" viewBox="0 0 1200 258">
    <polygon points="0,5 600,80 600,258 0,258" fill="#1a9fdf" opacity=".93"/>
    <polygon points="0,2 600,60 600,82 0,8" fill="var(--orange)"/>
    <polygon points="600,60 1200,0 1200,8 600,70" fill="#1a9fdf"/>
    <polygon points="600,70 1200,8 1200,258 600,258" fill="var(--orange-dark)" opacity=".95"/>
  </svg>
  <div class="feature" style="left:89px;top:564px"><h3>CELLULIT TREATMENT</h3><p>Nemo enim ipsam voluptatem quia voluptas sit aspernatur aut odit aut fugit, sed quia consequuntur magni dolores eos qui ratione voluptatem sequi nesciunt.</p></div>
  <div class="feature" style="left:637px;top:564px"><h3>FAT REMOVAL</h3><p>Nemo enim ipsam voluptatem quia voluptas sit aspernatur aut odit aut fugit, sed quia consequuntur magni dolores eos qui ratione voluptatem sequi nesciunt.</p></div>
</section>

<section>
  <h2 class="section-title" style="top:918px">ABOUT THE CLINIC</h2>
  <div class="title-rule" style="top:969px"></div>
  <p class="about-text">Nemo enim ipsam voluptatem quia voluptas sit aspernatur aut odit aut fugit, sed quia consequuntur magni dolores eos qui ratione voluptatem sequi nesciunt. Neque porro quisquam est, qui dolorem ipsum quia dolor sit amet, consectetur, adipisci velit, sed quia non numquam eius modi tempora incidunt ut labore et dolore magnam aliquam quaerat voluptatem.</p>
  <div class="btn btn-orange" style="left:470px;top:1122px;width:124px">Read More</div>
  <div class="btn btn-dark" style="left:606px;top:1122px;width:124px">Contact Us</div>
</section>

<section class="cryo">
  <h2>THE CRYOLIPOLYSIS</h2>
  <h4>TREATMENT:</h4>
  <p>It is a treatment freezing fat and cellulit, and this treatment will be the Attraction of the clinic. Nemo enim ipsam voluptatem quia voluptas sit aspernatur aut odit aut fugit, sed quia consequuntur magni dolores eos qui ratione voluptatem sequi nesciunt. Neque porro quisquam est, qui dolorem ipsum quia dolor sit amet, consectetur, adipisci velit, sed quia non numquam eius modi tempora incidunt ut labore et dolore magnam.</p>
  <div class="btn-outline" style="left:89px;top:335px;width:122px;height:44px;line-height:40px">Read More</div>
  <div class="video" role="img" aria-label="Video of a cryolipolysis treatment on a client's back">
    <div class="play"><svg width="56" height="56" viewBox="0 0 56 56"><polygon points="22,16 40,28 22,40" fill="#fff"/></svg></div>
  </div>
</section>

<section>
  <h2 class="section-title" style="top:1745px">OUR TESTIMONIALS</h2>
  <div class="title-rule" style="top:1793px"></div>

  <div class="quote" style="left:100px"><span class="quote-mark">“</span>Nemo enim ipsam voluptatem quia voluptas sit aspernatur aut odit aut fugit, sed quia consequuntur magni dolores eos qui ratione voluptatem sequi nesciunt.<span class="quote-tail"></span></div>
  <div class="quote featured" style="left:450px"><span class="quote-mark">“</span>Nemo enim ipsam voluptatem quia voluptas sit aspernatur aut odit aut fugit, sed quia consequuntur magni dolores eos qui ratione voluptatem sequi nesciunt.<span class="quote-tail"></span></div>
  <div class="quote" style="left:796px"><span class="quote-mark">“</span>Nemo enim ipsam voluptatem quia voluptas sit aspernatur aut odit aut fugit, sed quia consequuntur magni dolores eos qui ratione voluptatem sequi nesciunt.<span class="quote-tail"></span></div>

  <div class="author" style="left:100px"><span class="avatar" role="img" aria-label="Client portrait"></span><div><div class="author-name">Ida Halvorsen</div><div class="author-date">January 2, 2017</div></div></div>
  <div class="author featured" style="left:446px"><span class="avatar" role="img" aria-label="Client portrait"></span><div><div class="author-name">Camila Teixeira</div><div class="author-date">December 20, 2016</div></div></div>
  <div class="author" style="left:794px"><span class="avatar" role="img" aria-label="Client portrait"></span><div><div class="author-name">Sofie Lindqvist</div><div class="author-date">December 21, 2016</div></div></div>
</section>

<footer>
  <svg class="abs" style="left:70px;top:2209px" width="1060" height="38" viewBox="0 0 1060 38"><polygon points="19,0 0,0 19,38" fill="var(--blue-dark)"/><polygon points="1021,0 1041,0 1021,38" fill="var(--blue-dark)"/></svg>
  <div class="footer"></div>
  <div class="info-strip">
    <div class="info-cell"><span class="info-icon"><svg width="18" height="22" viewBox="0 0 18 22"><path d="M9 1a7 7 0 00-7 7c0 5 7 13 7 13s7-8 7-13a7 7 0 00-7-7z" fill="none" stroke="#fff" stroke-width="2"/><circle cx="9" cy="8" r="2.5" fill="#fff"/></svg></span><div><h5>HOSPITAL ADDRESS</h5><p>Strandvej 14, Nordhavn<br>København - 2100</p></div></div>
    <div class="info-cell mid"><span class="info-icon"><svg width="18" height="18" viewBox="0 0 24 24"><path fill="#fff" d="M6.6 10.8a15 15 0 006.6 6.6l2.2-2.2c.3-.3.7-.4 1-.2 1.1.4 2.3.6 3.6.6.6 0 1 .4 1 1V20c0 .6-.4 1-1 1A17 17 0 013 4c0-.6.4-1 1-1h3.5c.6 0 1 .4 1 1 0 1.3.2 2.5.6 3.6.1.3 0 .7-.2 1z"/></svg></span><div><h5>EMERGENCY ( 24X7 )</h5><p>Mobile: (+45) 140 318 7720<br>Toll Free : (+45) 140 318 7721</p></div></div>
    <div class="info-cell"><span class="info-icon"><svg width="20" height="16" viewBox="0 0 20 16"><rect x="1" y="1" width="18" height="14" rx="2" fill="#fff"/><path d="M1 2l9 7 9-7" stroke="var(--blue)" stroke-width="2" fill="none"/></svg></span><div><h5>Email id</h5><p>info@lumera.com</p></div></div>
  </div>

  <div class="footer-brand"><span class="brand-dot" style="background:var(--orange)"></span><span class="brand-name">Lumera</span></div>

  <div class="footer-col abs" style="left:366px;top:2370px;color:#fff">
    <h6>QUICK LINKS</h6><div class="rule"></div>
    <ul><li>› Lumera</li><li>› Behandlinger</li><li>› Produkter</li><li>› Priser</li><li>› Blog</li><li>› Kontakt</li></ul>
  </div>
  <div class="footer-col abs" style="left:555px;top:2370px;color:#fff">
    <h6>WORKING DAYS</h6><div class="rule"></div>
    <ul style="font-size:13px"><li style="margin-bottom:24px">Monday - Friday 8.00 - 18.00</li><li style="margin-bottom:24px">Saturday 8.00 - 18.00</li><li>Sunday 8.00 - 13.00</li></ul>
  </div>
  <div class="footer-col abs" style="left:821px;top:2370px;color:#fff">
    <h6>CONTACT FORM</h6><div class="rule"></div>
  </div>
  <div class="field" style="left:821px;top:2424px;width:131px;height:36px;color:#fff">Name</div>
  <div class="field" style="left:961px;top:2424px;width:132px;height:36px;color:#fff">Phone</div>
  <div class="field" style="left:821px;top:2467px;width:272px;height:66px;color:#fff">Message</div>
  <div class="send" style="color:#fff">SEND MESSAGE</div>

  <div class="footer-rule"></div>
  <div class="copyright" style="color:#fff">Copyright © 2017 Lumera. All Right Reserved</div>
  <span class="social" style="left:941px"></span>
  <span class="social" style="left:980px"></span>
  <span class="social" style="left:1019px"></span>
  <span class="social" style="left:1058px"></span>
</footer>

</body>
</html>
```